Wedding Ceremony Equipment Hire Business Card

I need a business card design for a new business I created called Vow Outfitters. We hire out Wedding Ceremony equipment and decorations mainly for beach and garden wedding ceremonies that include delivery, set up and dismantle. We do offer DIY Chair Hire as well.
I'd like to have a similar design and colours to our website:
www.vowoutfitters-example.com.au
If possible would like the front to incorporate our information and logo and the back to have two faded example pictures of our wedding ceremonies.
I have attached two photos and our logo. Please let me know if you need a better pic of our logo though.

Target Market(s)

Newly engaged couples, aged 25 and upwards

Industry/Entity Type

Wedding

Contact Information for Business Card

Vow Outfitters
Merel Thorpe
0491 870 264
vowoutfitters@mailbox-example.com
www.social-example.com/VowOutfitters

```html
<!DOCTYPE html>
<html lang="en">
<head>
<meta charset="utf-8">
<title>Vow Outfitters – Business Card</title>
<link rel="stylesheet" href="https://fonts.googleapis.com/css2?family=Open+Sans:wght@400;600&display=swap">
<style>
  :root {
    --teal-light: #6cc0cf;
    --teal-mid: #4f9aa3;
    --teal-deep: #2f6a70;
    --teal-shadow: #3f7e85;
    --white: #ffffff;
    --name-red: #c3272f;
    --ink: #1c1c1c;
    --sky: #3f86d6;
    --grass: #3f6b2c;
    --sand: #c79a5e;
  }
  * { box-sizing: border-box; margin: 0; padding: 0; }
  html, body {
    width: 1167px; height: 1200px; overflow: hidden;
    background: var(--teal-mid);
    font-family: "Open Sans", Arial, sans-serif;
  }
  .card {
    position: relative; width: 1167px; height: 1200px;
    background: linear-gradient(180deg, var(--teal-deep) 0%, var(--teal-mid) 35%, var(--teal-light) 55%, var(--teal-mid) 75%, var(--teal-deep) 100%);
  }
  .front {
    position: absolute; left: 0; top: 0; width: 1167px; height: 617px;
  }
  .front-left {
    position: absolute; left: 0; top: 0; width: 571px; height: 617px;
    background: linear-gradient(180deg, var(--teal-light) 0%, var(--teal-shadow) 30%, var(--teal-mid) 55%, var(--teal-light) 100%);
  }
  .front-right {
    position: absolute; left: 571px; top: 0; width: 596px; height: 617px;
    background: radial-gradient(ellipse at 30% 30%, var(--teal-light) 0%, var(--teal-mid) 45%, var(--teal-deep) 100%);
    box-shadow: -6px 0 12px rgba(0,0,0,0.3);
  }
  .name-label {
    position: absolute; left: 145px; top: 224px; width: 426px; height: 167px;
    background: linear-gradient(180deg, #ffffff 0%, #f4f4f4 70%, #dcdcdc 100%);
    border-radius: 26px 0 0 26px;
    box-shadow: -2px 3px 6px rgba(0,0,0,0.35);
    text-align: center;
  }
  .person-name {
    margin-top: 20px;
    font-size: 50px; font-weight: 400; color: var(--name-red);
    letter-spacing: 1px;
  }
  .business-name {
    margin-top: 4px;
    font-size: 30px; font-weight: 600; color: var(--ink);
  }
  .contact-list {
    position: absolute; left: 610px; top: 232px; list-style: none;
    color: var(--white); font-size: 25px; letter-spacing: 0.5px;
  }
  .contact-list li { height: 60px; line-height: 40px; }
  .contact-list li::before { content: "| "; opacity: 0.85; }
  .divider {
    position: absolute; left: 0; top: 617px; width: 1167px; height: 2px;
    background: rgba(255,255,255,0.85);
  }
  .photo {
    position: absolute; top: 646px; height: 526px;
  }
  .photo-garden {
    left: 27px; width: 555px;
    background: linear-gradient(180deg, var(--sky) 0%, #8fb8dc 30%, #5d8a4e 50%, var(--grass) 75%, #2f4f22 100%);
  }
  .photo-beach {
    left: 582px; width: 554px;
    background: linear-gradient(180deg, #1f5fc4 0%, var(--sky) 30%, #e6e6e6 50%, var(--sand) 70%, #b08148 100%);
  }
</style>
</head>
<body>
<main class="card">
  <section class="front">
    <div class="front-left"></div>
    <div class="front-right"></div>
    <div class="name-label">
      <p class="person-name">Merel Thorpe</p>
      <p class="business-name">Vow Outfitters</p>
    </div>
    <ul class="contact-list">
      <li>0491 870 264</li>
      <li>vowoutfitters@mailbox-example.com</li>
      <li>www.vowoutfitters-example.com.au</li>
      <li>www.social-example.com/VowOutfitters</li>
    </ul>
  </section>
  <div class="divider"></div>
  <section class="back">
    <div class="photo photo-garden" role="img" aria-label="Photo of a harbourside garden wedding ceremony with white chairs and a white aisle runner"></div>
    <div class="photo photo-beach" role="img" aria-label="Photo of a beach wedding ceremony with white chairs and a woven aisle runner on the sand"></div>
  </section>
</main>
</body>
</html>
```